We have a cheerleading competition on Sunday the 30 and I want to encourage parent assistance, support and participation!
Updates

1. Please add:
    Cheer Championship (instead of Cheerleading Competition)

2. Banner: Let's support our Cheerleaders!

Under Banner have the Date in big

Before the Location add:  Joins us at:

Thank you all for your designs and taking the time to submit them. I greatly appreciate them and they were all lovely. I could only pick one though! Hope to have you again on my next project.

Regards, Dariela

Requirements
Must have
• Flyer should be 1/2 of an A4 page. kid friendly. The cheerleaders are 6-13 yrs old.
The colors Burgundy, Gold (yellow) and White - It should have the team Eagle design on it. Bayview Ridge Otters

Simple design. It will contain an address, times and dates.

should have all of the following information:

Date: Sunday - October 30th 2011
Location: Harbor Crest Arena at the Coastal Pines College
3870 Pellman Lane
Palm Haven, FL 34120
Time: Tickets on sale 8:30AM - Doors Open 9:00AM Starts: 10:00AM
Prices: Adults $10.00 Children $5.00 - Cash Only

```html
<!DOCTYPE html>
<html lang="en">
<head>
<meta charset="utf-8">
<title>Cheer Championship Flyers</title>
<link rel="stylesheet" href="https://fonts.googleapis.com/css2?family=Arimo:wght@400;700&family=Lilita+One&display=swap">
<style>
:root{
  --red:#d31f26;
  --red-dark:#a3141a;
  --orange:#f06a1f;
  --gold:#f8b527;
  --ink:#231f20;
  --white:#ffffff;
  --frame:#6d6e71;
  --ribbon-shade:#bcbec0;
}
*{margin:0;padding:0;box-sizing:border-box}
html,body{width:1200px;height:900px;overflow:hidden;background:var(--white)}
body{position:relative;font-family:"Arimo",Arial,sans-serif;color:var(--red)}
.flyer{position:absolute;background:var(--white);border:1px solid var(--frame);overflow:hidden}
.flyer--portrait{left:13px;top:110px;width:479px;height:683px}
.flyer--landscape{left:504px;top:233px;width:683px;height:479px}
.swooshes{position:absolute;inset:0;width:100%;height:100%}
.abs{position:absolute}
.title{font-family:"Lilita One",sans-serif;color:var(--red);line-height:1;white-space:nowrap;
  -webkit-text-stroke:5px var(--white);paint-order:stroke fill;
  text-shadow:3px 3px 0 var(--ink),4px 4px 0 var(--ink);transform:rotate(-4deg);transform-origin:left center}
.ribbon{position:absolute}
.ribbon-text{position:absolute;font-family:"Lilita One",sans-serif;color:var(--white);white-space:nowrap;transform:rotate(-6deg);transform-origin:left center}
.cheerleader{position:absolute;background:var(--red);border-radius:45% 45% 40% 40%;opacity:.9}
.day{font-weight:700;line-height:1;text-align:center;white-space:nowrap}
.date{font-weight:700;line-height:1;text-align:center;white-space:nowrap}
.label{font-weight:700;text-align:center;white-space:nowrap;line-height:1}
.info-box{position:absolute;border-radius:16px;font-weight:700;line-height:1.22;white-space:nowrap}
.info-box .street{letter-spacing:.5px}
.times{font-weight:700;line-height:1.25}
.times div{display:flex;justify-content:space-between}
.prices{font-weight:700;text-align:center;line-height:1.35;white-space:nowrap}
.team{position:absolute;display:flex;align-items:center;font-weight:700;color:var(--ink);white-space:nowrap}
.team-dot{border-radius:50%;background:var(--red-dark)}
</style>
</head>
<body>

<section class="flyer flyer--portrait">
  <svg class="swooshes" viewBox="0 0 479 683">
    <path d="M-10,120 Q70,20 240,-12" fill="none" stroke="var(--gold)" stroke-width="48"/>
    <path d="M-10,255 Q130,50 330,-12" fill="none" stroke="var(--gold)" stroke-width="20"/>
    <path d="M-10,225 Q235,320 258,700" fill="none" stroke="var(--gold)" stroke-width="30"/>
  </svg>

  <div class="cheerleader" role="img" aria-label="Cheerleader silhouette with pom-poms" style="left:315px;top:60px;width:130px;height:115px"></div>

  <div class="title abs" style="left:127px;top:104px;font-size:66px">Cheer</div>
  <div class="title abs" style="left:37px;top:166px;font-size:64px">Championship</div>

  <svg class="ribbon" style="left:82px;top:200px" width="390" height="100" viewBox="0 0 390 100">
    <defs><linearGradient id="ribbon-portrait" x1="0" x2="1"><stop offset="0" stop-color="var(--red-dark)"/><stop offset=".6" stop-color="var(--red)"/><stop offset="1" stop-color="var(--orange)"/></linearGradient></defs>
    <path d="M18,62 Q190,50 385,22 L380,60 Q200,95 30,92 Z" fill="var(--ribbon-shade)"/>
    <path d="M10,45 Q190,32 388,2 L382,48 Q200,80 22,84 Q28,62 10,45 Z" fill="url(#ribbon-portrait)"/>
  </svg>
  <div class="ribbon-text" style="left:112px;top:242px;font-size:19px">Let's support our Cheerleaders!</div>

  <div class="cheerleader" role="img" aria-label="Jumping cheerleader silhouette with pom-poms" style="left:38px;top:305px;width:105px;height:185px"></div>

  <div class="day abs" style="left:175px;top:316px;width:160px;font-size:30px">Sunday</div>
  <div class="date abs" style="left:165px;top:348px;width:180px;font-size:17px">October 30th 2011</div>

  <div class="label abs" style="left:295px;top:382px;width:150px;font-size:19px;font-weight:400">Join us at:</div>
  <div class="info-box" style="left:260px;top:409px;width:196px;height:99px;border:4px solid var(--gold);padding:8px 0 0 11px;font-size:14px">
    <div>Harbor Crest Arena at</div>
    <div>the Coastal Pines College</div>
    <div class="street" style="font-size:16px">3870 Pellman Lane</div>
    <div>Palm Haven, FL 34120</div>
  </div>

  <div class="label abs" style="left:282px;top:518px;width:150px;font-size:18px">Time:</div>
  <div class="info-box times" style="left:260px;top:542px;width:196px;height:89px;border:4px solid var(--gold);padding:18px 18px 0 15px;font-size:14px">
    <div><span>Tickets on sale</span><span>8:30AM</span></div>
    <div><span>Doors Open</span><span>9:00AM</span></div>
    <div><span>Starts:</span><span>10:00AM</span></div>
  </div>

  <div class="prices abs" style="left:20px;top:506px;width:170px;font-size:10px">
    <div style="font-size:13px">Prices:</div>
    <div>Adults $10.00</div>
    <div>Children $5.00 - Cash Only</div>
  </div>

  <div class="team" style="left:24px;top:600px;flex-direction:column;gap:10px;width:160px">
    <span class="team-dot" style="width:36px;height:36px"></span>
    <span style="font-size:12px">Bayview Ridge Otters</span>
  </div>
</section>

<section class="flyer flyer--landscape">
  <svg class="swooshes" viewBox="0 0 683 479">
    <path d="M-10,420 Q150,170 600,-12" fill="none" stroke="var(--gold)" stroke-width="36"/>
    <path d="M430,490 Q510,340 700,318" fill="none" stroke="var(--gold)" stroke-width="34"/>
    <path d="M540,490 Q590,390 700,372 L700,490 Z" fill="var(--gold)"/>
    <path d="M560,70 Q640,45 700,60 L700,20 Q630,15 560,70 Z" fill="var(--gold)"/>
  </svg>

  <div class="team" style="left:38px;top:32px;flex-direction:column;gap:18px;width:120px">
    <span class="team-dot" style="width:40px;height:40px"></span>
    <span style="font-size:10px">Bayview Ridge Otters</span>
  </div>

  <div class="cheerleader" role="img" aria-label="Cheerleader silhouette with pom-poms" style="left:430px;top:20px;width:95px;height:105px"></div>

  <div class="title abs" style="left:228px;top:50px;font-size:62px">Cheer</div>
  <div class="title abs" style="left:154px;top:108px;font-size:62px">Championship</div>

  <svg class="ribbon" style="left:208px;top:150px" width="412" height="85" viewBox="0 0 390 85">
    <defs><linearGradient id="ribbon-landscape" x1="0" x2="1"><stop offset="0" stop-color="var(--red-dark)"/><stop offset=".6" stop-color="var(--red)"/><stop offset="1" stop-color="var(--orange)"/></linearGradient></defs>
    <path d="M18,55 Q190,44 385,20 L380,55 Q200,82 30,80 Z" fill="var(--ribbon-shade)"/>
    <path d="M10,40 Q190,28 388,2 L382,42 Q200,68 22,72 Q28,55 10,40 Z" fill="url(#ribbon-landscape)"/>
  </svg>
  <div class="ribbon-text" style="left:236px;top:190px;font-size:17px">Let's support our Cheerleaders!</div>

  <div class="label abs" style="left:498px;top:224px;width:110px;font-size:14px;font-weight:400">Join us at:</div>
  <div class="info-box" style="left:459px;top:243px;width:170px;height:85px;border:3px solid var(--red);padding:8px 0 0 9px;font-size:12px">
    <div>Harbor Crest Arena at</div>
    <div>the Coastal Pines College</div>
    <div class="street" style="font-size:13.5px">3870 Pellman Lane</div>
    <div>Palm Haven, FL 34120</div>
  </div>

  <div class="day abs" style="left:278px;top:249px;width:120px;font-size:24px">Sunday</div>
  <div class="date abs" style="left:265px;top:276px;width:148px;font-size:14px">October 30th 2011</div>

  <div class="cheerleader" role="img" aria-label="Jumping cheerleader silhouette with pom-poms" style="left:120px;top:240px;width:125px;height:185px"></div>

  <div class="label abs" style="left:296px;top:309px;width:80px;font-size:13px">Time:</div>
  <div class="times abs" style="left:263px;top:326px;width:158px;font-size:13px;font-weight:400;line-height:1.3">
    <div><span>Tickets on sale</span><span>8:30AM</span></div>
    <div><span>Doors Open</span><span>9:00AM</span></div>
    <div><span>Starts:</span><span>10:00AM</span></div>
  </div>

  <div class="prices abs" style="left:256px;top:388px;width:170px;font-size:11px">
    <div style="font-size:13px">Prices:</div>
    <div>Adults $10.00</div>
    <div>Children $5.00 - Cash Only</div>
  </div>
</section>

</body>
</html>
```